We TEND toward Wedlock Event

I need a flyer to promote an Event we do that promotes Marriage and asks people to get involved in Ministry to Marriage. I need a graphic with the words: "We TEND toward Wedlock!"

Target Market(s)

Potential volunteers to get involve in the marriage ministry in a particular Catholic Parish.

Industry/Entity Type

Ministry

Logo Text

We TEND toward Wedlock!

Colors

Designer to choose colors to be used in the design.

Requirements
Must have
• Under the graphic should be the words: "An Event to Encourage and Support Marriages in our Parish"
• There could be a picture or pictures of married couples at different ages/stages.
• Other words include:
• "Please join us as we discuss the realities facing married couples today and what our response as a Parish can and should be."
• I also need a place to put name of Parish, date, time and location. This information will change for each event so the actual information will need to be left blank.
Nice to have
• Please make it eye-catching and something that would like to attend.
• WE hope the logo itself is fun and colorful.
• Would also like our non-profit logo along with the words "Conducted By..."(HearthWeaving USA) somewhere on flyer.

```html
<!DOCTYPE html>
<html lang="en">
<head>
<meta charset="utf-8">
<title>We TEND toward Wedlock – Parish Event Flyer</title>
<link rel="stylesheet" href="https://fonts.googleapis.com/css2?family=Belleza&family=Marcellus&family=Marck+Script&display=swap">
<style>
  :root {
    --bg-edge: #d6d0c1;
    --bg-mid: #e6e1d6;
    --bg-glow: #faf8f3;
    --ink: #1c1c1c;
    --body-ink: #4a4945;
    --rose: #e3a1b4;
    --rose-label: #d98ca6;
    --frame: #bdb8ab;
    --paper: #ffffff;
    --brand-ink: #1f3a3a;
  }
  * { margin: 0; padding: 0; box-sizing: border-box; }
  html, body { width: 927px; height: 1200px; overflow: hidden; }
  body { background: var(--bg-edge); }

  .flyer {
    position: relative;
    width: 927px;
    height: 1200px;
    overflow: hidden;
    background:
      linear-gradient(90deg, var(--bg-edge) 0%, var(--bg-mid) 30%, var(--bg-glow) 48%, var(--bg-glow) 52%, var(--bg-mid) 70%, var(--bg-edge) 100%);
    font-family: "Belleza", sans-serif;
  }

  .event-title {
    position: absolute;
    top: 118px;
    left: 0;
    width: 927px;
    text-align: center;
    font-family: "Belleza", sans-serif;
    font-weight: 400;
    font-size: 70px;
    line-height: 76px;
    color: var(--ink);
  }

  .tagline {
    position: absolute;
    top: 206px;
    left: 0;
    width: 927px;
    text-align: center;
    font-family: "Marck Script", cursive;
    font-size: 46px;
    line-height: 54px;
    color: var(--ink);
  }

  .event-purpose {
    position: absolute;
    top: 276px;
    left: 0;
    width: 927px;
    text-align: center;
    font-family: "Belleza", sans-serif;
    font-size: 21px;
    line-height: 28px;
    color: var(--body-ink);
  }

  .photo-strip {
    position: absolute;
    top: 333px;
    left: 0;
    width: 927px;
    height: 246px;
    background: var(--rose);
  }
  .photo {
    position: absolute;
    top: 19px;
    height: 208px;
  }
  .photo--couple {
    left: 0; width: 302px;
    background: linear-gradient(160deg, #f3f1ee 0%, #e8e4de 45%, #c9bfb5 100%);
  }
  .photo--church {
    left: 304px; width: 319px;
    background: linear-gradient(180deg, #d9c7a8 0%, #b7935f 45%, #5a3a24 100%);
  }
  .photo--rings {
    left: 625px; width: 302px;
    background: linear-gradient(200deg, #b7a48d 0%, #e4ded4 40%, #f2efe9 100%);
  }

  .invitation {
    position: absolute;
    top: 600px;
    left: 0;
    width: 927px;
    text-align: center;
    font-family: "Belleza", sans-serif;
    font-size: 30px;
    line-height: 36px;
    color: var(--body-ink);
  }

  .details-frame {
    position: absolute;
    top: 726px;
    left: 122px;
    width: 672px;
    height: 328px;
    background: var(--frame);
    padding: 8px;
  }
  .details-card {
    width: 100%;
    height: 100%;
    background: var(--paper);
    padding: 40px 0 0 42px;
  }
  .details-label {
    font-family: "Marcellus", serif;
    font-size: 32px;
    line-height: 32px;
    color: var(--rose-label);
    margin-bottom: 33px;
  }

  .conducted {
    position: absolute;
    top: 1094px;
    left: 238px;
    font-family: "Marck Script", cursive;
    font-size: 25px;
    line-height: 32px;
    color: var(--ink);
  }

  .host-mark {
    position: absolute;
    top: 1096px;
    left: 405px;
    display: flex;
    align-items: center;
    gap: 12px;
  }
  .host-mark__square {
    width: 34px;
    height: 34px;
    background: var(--brand-ink);
  }
  .host-mark__name {
    font-family: "Belleza", sans-serif;
    font-size: 26px;
    line-height: 34px;
    color: var(--brand-ink);
  }
</style>
</head>
<body>
  <main class="flyer">
    <h1 class="event-title">HearthWeaving USA</h1>
    <p class="tagline">We TEND toward Wedlock!</p>
    <p class="event-purpose">An Event to Encourage and Support Marriages in our Parish</p>

    <section class="photo-strip">
      <div class="photo photo--couple" role="img" aria-label="Bride and groom forming a heart with their hands"></div>
      <div class="photo photo--church" role="img" aria-label="Wedding ceremony at the altar of an ornate church"></div>
      <div class="photo photo--rings" role="img" aria-label="Two wedding rings resting on an open Bible"></div>
    </section>

    <p class="invitation">
      Please join us as we discuss<br>
      the realities facing married couples today<br>
      and what our response as a Parish can and should be!
    </p>

    <section class="details-frame">
      <div class="details-card">
        <p class="details-label">PARISH:</p>
        <p class="details-label">DATE:</p>
        <p class="details-label">TIME:</p>
        <p class="details-label">LOCATION:</p>
      </div>
    </section>

    <p class="conducted">Conducted by:</p>
    <div class="host-mark">
      <span class="host-mark__square"></span>
      <span class="host-mark__name">HearthWeaving USA</span>
    </div>
  </main>
</body>
</html>
```